Institutional website for an IT Consulting company

Web design + HTML + CSS / Bootstrap + JS (interaction) integration in order to extend our existing website brisklane.coop.
Our website is currently aiming only for recruitment and not for customers, we want to provide a fluid transition between customer side website (this project) and recruitment website (existing site).

Ideally we would love the new design to be "inspired" by our actual graphic chart (Colors mainly). It should provide a great user experience and a landing page (or any mean) allowing the visitor to easily switch from the end customer front end (this project), the recruitment front end (existing front end https://www.brisklane.coop/) and the existing member front end (an other existing front end dedicated to members already existing).

In attachment you will find the expected site content mainly a one page with a first level of information and "link" to sub pages (a way to directly access this sub pages should also be provided).

The website should be accessible on mobile device and desktop.

The attachment is in french as it reflect the final site content, but if google translate isn't sufficient to have a general idea of the content, feel free to ask. We would love to have some visual representation for some categories.

Target Market(s)

fortune 500 companies

Industry/Entity Type

It Company

Coding

Coded - Design and coding required

Number of Pages Required

5+ page

Requirements
Must have
• This project must have an easy way to navigate between 3 sub sites, the customer one (the one designed here), the consultant / recruitment one (the existing one at brisklane.coop), the members one.

A one page experience at first leading to detail pages.

Custom made visuals to illustrate each categories.

Inspiration websites : plovu[.]fr ; tarnsby[.]com ; qolvari[.] com ...

Be inspired by the existing color from our logo and existing website at brisklane[.]coop

```html
<!DOCTYPE html>
<html lang="en">
<head>
<meta charset="utf-8">
<title>Brisklane.coop — IT Consulting</title>
<link href="https://fonts.googleapis.com/css2?family=Montserrat:wght@500;600;700;800&family=Open+Sans:ital,wght@0,400;0,600;1,400&display=swap" rel="stylesheet">
<style>
:root{
  --teal:#12b3bf;
  --teal-light:#3cc6cf;
  --teal-soft:#6fd3da;
  --ink:#0d3b3a;
  --dark:#333333;
  --text:#7a7a7a;
  --heading:#6b6b6b;
  --rule:#d9d9d9;
  --avatar:#cccccc;
  --badge:#eceaf1;
  --white:#ffffff;
}
*{margin:0;padding:0;box-sizing:border-box}
html,body{width:1200px;height:3069px;overflow:hidden;background:var(--white)}
body{position:relative;font-family:"Open Sans",sans-serif;color:var(--text)}
.abs{position:absolute}
a{color:inherit;text-decoration:none}

/* header */
.brand{font-family:"Montserrat",sans-serif;font-weight:800;color:var(--ink);font-size:29px;letter-spacing:.5px;display:flex;align-items:center;gap:10px;white-space:nowrap}
.brand .mark{width:18px;height:18px;background:var(--teal)}
.top-links{right:112px;top:16px;font-family:"Montserrat",sans-serif;font-weight:500;font-size:15px;color:var(--dark);display:flex;gap:10px;align-items:center}
.top-links svg{vertical-align:-2px;margin-right:5px}
.nav-btn{top:50px;height:49px;border:2px solid #8a8a8a;font-family:"Montserrat",sans-serif;font-weight:600;font-size:15px;color:#777;display:flex;align-items:center;justify-content:center;white-space:nowrap}
.nav-btn.primary{background:var(--dark);border-color:var(--dark);color:var(--white)}

/* hero */
.hero{left:0;top:122px;width:1200px;height:404px;background:linear-gradient(100deg,#4a3a33 0%,#7d6b60 30%,#c9c3bb 55%,#6d5a52 78%,#5a2c36 100%)}
.hero-title{left:81px;top:250px;font-family:"Montserrat",sans-serif;font-weight:800;color:var(--white);line-height:1}
.hero-title .l1{font-size:55px;display:block}
.hero-title .l2{font-size:73px;display:block;margin-top:14px}
.dots{left:549px;top:466px;display:flex;gap:11px}
.dots span{width:17px;height:17px;border-radius:50%;border:2px solid #444}
.dots span.on{background:#555}

/* about */
.badge{left:110px;top:608px;width:379px;height:448px;background:var(--badge)}
.about-text{left:541px;top:596px;width:548px;font-size:15px;line-height:27.4px}
.about-text p+p{margin-top:27.4px}
.team-intro{left:140px;top:1118px;width:920px;text-align:center;font-size:26px;line-height:42px;color:var(--heading);font-weight:600}

/* team */
.photo-frame{width:369px;height:381px;background:var(--teal);padding:25px}
.photo-frame .inner{width:100%;height:100%;background:var(--white);padding:8px}
.photo-frame .pic{width:100%;height:100%;background:var(--avatar);overflow:hidden}
.member-name{font-size:33px;color:var(--heading);font-weight:600}
.member-text{font-size:14.5px;line-height:27.4px;width:545px}
.contact-line{font-family:"Montserrat",sans-serif;font-size:17px;color:#666;display:flex;align-items:center;gap:12px;font-weight:500}

/* testimonials */
.testimonials{left:0;top:2144px;width:1200px;height:510px;background:var(--teal);overflow:hidden}
.testimonials .shade{position:absolute;background:rgba(255,255,255,.05)}
.t-title{left:0;width:1200px;top:2196px;text-align:center;font-family:"Montserrat",sans-serif;font-weight:800;font-size:43px;color:var(--white)}
.client{top:2313px;width:183px;height:86px;border:5px solid var(--teal-soft);display:flex;align-items:center;justify-content:center;gap:8px;font-family:"Montserrat",sans-serif;font-weight:700;font-size:26px;color:var(--teal-soft);white-space:nowrap}
.client .sq{width:16px;height:16px;background:var(--teal-soft)}
.client.active{border-color:var(--white);color:var(--white);letter-spacing:3px;font-size:23px}
.t-rule{left:110px;top:2445px;width:978px;height:1px;background:var(--teal-light)}
.avatar{left:110px;top:2470px;width:119px;height:119px;border-radius:50%;background:radial-gradient(circle at 50% 40%,#d9b9a0,#8f7a6c 60%,#e8e8e8)}
.t-name{left:256px;top:2500px;font-size:19px;line-height:31px;color:var(--white)}
.t-quote{left:385px;top:2488px;width:700px;font-style:italic;font-size:16.5px;line-height:27.5px;color:var(--white)}

/* footer */
.f-col h4{font-family:"Open Sans",sans-serif;font-weight:600;font-size:19px;color:#555;margin-bottom:10px}
.f-col li{list-style:none;font-size:14.5px;line-height:26.6px;color:#777}
.f-find li{display:flex;gap:10px}
.f-rule{left:110px;top:2985px;width:978px;height:1px;background:var(--rule)}
.copy{left:110px;top:3017px;font-size:15px;color:#888}
.social{top:3005px;width:43px;height:43px;border-radius:50%;border:1.5px solid var(--teal)}
</style>
</head>
<body>

<header>
  <a class="abs brand" style="left:110px;top:40px" href="https://www.brisklane.coop/"><span class="mark"></span>BRISKLANE.COOP</a>
  <div class="abs top-links">
    <a href="#"><svg width="11" height="13" viewBox="0 0 11 13"><rect x="0" y="5" width="11" height="8" rx="1" fill="#12b3bf"/><path d="M2.5 5V3.5a3 3 0 016 0V5" stroke="#12b3bf" stroke-width="1.8" fill="none"/></svg>LOG IN</a>
    <span>|</span>
    <a href="#"><svg width="13" height="13" viewBox="0 0 13 13"><circle cx="6.5" cy="6.5" r="6.5" fill="#12b3bf"/><text x="6.5" y="10" font-size="9" text-anchor="middle" fill="#fff" font-family="Montserrat,sans-serif" font-weight="700">?</text></svg>HELP</a>
  </div>
  <a class="abs nav-btn" style="left:530px;width:149px" href="#">I AM BRISKLANE</a>
  <a class="abs nav-btn" style="left:697px;width:242px" href="#">I WISH TO JOIN BRISKLANE</a>
  <a class="abs nav-btn primary" style="left:956px;width:131px" href="#">CONTACT US</a>
</header>

<section>
  <div class="abs hero" role="img" aria-label="Photo of a team gathered around a table with documents and a coffee mug"></div>
  <h1 class="abs hero-title"><span class="l1">EXPERTS IN</span><span class="l2">THEIR FIELD</span></h1>
  <div class="abs dots"><span class="on"></span><span></span><span></span><span></span></div>
</section>

<section>
  <div class="abs badge" role="img" aria-label="Training quality certification badge"></div>
  <div class="abs about-text">
    <p>Combining junior experiences to more than 15 years of data projects in Corvane's environments, Brisklane is able to take over all the standard steps of a MOE project. With half certified consultants on 35 different certifications, Brisklane has a great added value on all data platform issues encountered in Corvane tools. Operational on cost-plus contracts for long-term missions as well as punctual audit contracts, we provide support to product deployment such as Corvane Lens.</p>
    <p>The QualiDoc agreements, and specially the recognition of CCT valuate our skills on training your staff and the funding opportunities of these trainings.</p>
    <p>Last particular aspect, our reseller Corvane CRP status allows us to provide Corvane Suite licences and Corvane Cloud consumption credit, while providing support in data deployment on these infrastructure. With a specific monitoring of your licences, whether you have 10 or 1 000 users, feel free to contact us on our CRP program @</p>
  </div>
  <p class="abs team-intro">Our commercial and administrative team is also at your service, but also to S/E in order to assist them on daily tasks.</p>
</section>

<section>
  <div class="abs photo-frame" style="left:112px;top:1238px"><div class="inner"><div class="pic" role="img" aria-label="Placeholder portrait of Maëlle"></div></div></div>
  <h3 class="abs member-name" style="left:546px;top:1228px">Maëlle</h3>
  <p class="abs member-text" style="left:547px;top:1294px">Sed ut perspiciatis unde omnis iste natus error sit voluptatem accusan tium doloremque laudantium, totam rem aperiam, eaque ipsa quae ab illo inventore veritatis et quasi architecto beatae vitae dicta sunt modi tempora incidunt ut labore et dolore magnam aliquam quaerat volup tate &nbsp;im ad minima veniam, quis nostrum exercitationem ullam corporis suscipit laboriosam, nisi ut aliquid ex ea commodi consequat is autem vel eum iure reprehenderiexplicabo volup tate velit esse quam nihil molestiae consequa.</p>
  <div class="abs contact-line" style="left:547px;top:1520px"><svg width="14" height="14" viewBox="0 0 14 14"><path d="M3 1l2.5 3-1.5 1.5a8 8 0 004.5 4.5L10 8.5l3 2.5-1.5 2.5C6 13 1 8 .5 2.5z" fill="#12b3bf"/></svg>1 888 888 8888</div>
  <div class="abs contact-line" style="left:547px;top:1556px"><svg width="18" height="13" viewBox="0 0 18 13"><rect width="18" height="13" rx="1" fill="#12b3bf"/><path d="M1 1l8 6 8-6" stroke="#fff" stroke-width="1.5" fill="none"/></svg>maelle@brisklane.coop</div>

  <h3 class="abs member-name" style="left:108px;top:1674px">Noémie</h3>
  <p class="abs member-text" style="left:110px;top:1740px">Sed ut perspiciatis unde omnis iste natus error sit voluptatem accusan tium doloremque laudantium, totam rem aperiam, eaque ipsa quae ab illo inventore veritatis et quasi architecto beatae vitae dicta sunt modi tempora incidunt ut labore et dolore magnam aliquam quaerat volup tate &nbsp;im ad minima veniam, quis nostrum exercitationem ullam corporis suscipit laboriosam, nisi ut aliquid ex ea commodi consequat is autem vel eum iure reprehenderiexplicabo volup tate velit esse quam nihil molestiae consequa.</p>
  <div class="abs contact-line" style="left:110px;top:1966px"><svg width="14" height="14" viewBox="0 0 14 14"><path d="M3 1l2.5 3-1.5 1.5a8 8 0 004.5 4.5L10 8.5l3 2.5-1.5 2.5C6 13 1 8 .5 2.5z" fill="#12b3bf"/></svg>1 888 888 8888</div>
  <div class="abs contact-line" style="left:110px;top:2002px"><svg width="18" height="13" viewBox="0 0 18 13"><rect width="18" height="13" rx="1" fill="#12b3bf"/><path d="M1 1l8 6 8-6" stroke="#fff" stroke-width="1.5" fill="none"/></svg>noemie@brisklane.coop</div>
  <div class="abs photo-frame" style="left:717px;top:1684px"><div class="inner"><div class="pic" role="img" aria-label="Placeholder portrait of Noémie"></div></div></div>
</section>

<section>
  <div class="abs testimonials">
    <div class="shade" style="left:790px;top:0;width:410px;height:510px"></div>
    <div class="shade" style="left:880px;top:110px;width:240px;height:320px"></div>
  </div>
  <h2 class="abs t-title">CLIENT TESTIMONIALS</h2>
  <svg class="abs" style="left:66px;top:2342px" width="16" height="28" viewBox="0 0 16 28"><path d="M14 2L3 14l11 12" stroke="#9fe2e7" stroke-width="3" fill="none"/></svg>
  <div class="abs client" style="left:110px"><span class="sq"></span>KESTRO</div>
  <div class="abs client" style="left:309px"><span class="sq"></span>KESTRO</div>
  <div class="abs client active" style="left:508px">VELMORE</div>
  <div class="abs client" style="left:705px"><span class="sq"></span>KESTRO</div>
  <div class="abs client" style="left:904px"><span class="sq"></span>KESTRO</div>
  <svg class="abs" style="left:1106px;top:2342px" width="16" height="28" viewBox="0 0 16 28"><path d="M2 2l11 12L2 26" stroke="#ffffff" stroke-width="3" fill="none"/></svg>
  <div class="abs t-rule"></div>
  <div class="abs avatar" role="img" aria-label="Client portrait photo"></div>
  <p class="abs t-name">John Doe<br>CEO</p>
  <p class="abs t-quote">“Nam libero tempore, cum soluta nobis est eligendi opticum que nihil impedit quo minus id quod maxime placeat facere possimus, omnis voluptas assumenda est, omnis dolor rep ellendu autem quibusdam et aut .”</p>
</section>

<footer>
  <a class="abs brand" style="left:110px;top:2800px" href="https://www.brisklane.coop/"><span class="mark"></span>BRISKLANE.COOP</a>
  <div class="abs f-col" style="left:468px;top:2700px">
    <h4>Information</h4>
    <ul><li>About us</li><li>Team</li><li>Jobs</li><li>Hurry</li><li>Freelancing news</li><li>Data protection</li><li>Help</li><li>Sitemap</li></ul>
  </div>
  <div class="abs f-col" style="left:673px;top:2700px">
    <h4>Quick Links</h4>
    <ul><li>Offers and prices</li><li>Company</li><li>Open Brisklane coop</li><li>Insights</li><li>Create my Profile</li></ul>
  </div>
  <div class="abs f-col f-find" style="left:879px;top:2700px">
    <h4>Find Us</h4>
    <ul>
      <li><svg width="11" height="15" viewBox="0 0 11 15" style="margin-top:6px"><path d="M5.5 0A5.5 5.5 0 000 5.5C0 9.5 5.5 15 5.5 15S11 9.5 11 5.5A5.5 5.5 0 005.5 0z" fill="#12b3bf"/><circle cx="5.5" cy="5.5" r="2" fill="#fff"/></svg><span>14 Rue des Tanneurs<br>75011 Paris</span></li>
      <li style="margin-top:28px"><svg width="14" height="14" viewBox="0 0 14 14" style="margin-top:6px"><path d="M3 1l2.5 3-1.5 1.5a8 8 0 004.5 4.5L10 8.5l3 2.5-1.5 2.5C6 13 1 8 .5 2.5z" fill="#12b3bf"/></svg>01 84 20 61 73</li>
      <li style="margin-top:28px"><svg width="18" height="13" viewBox="0 0 18 13" style="margin-top:7px"><rect width="18" height="13" rx="1" fill="#12b3bf"/><path d="M1 1l8 6 8-6" stroke="#fff" stroke-width="1.5" fill="none"/></svg>contact@brisklane.coop</li>
    </ul>
  </div>
  <div class="abs f-rule"></div>
  <p class="abs copy">© 2020, Brisklane.coop.</p>
  <a class="abs social" style="left:945px" href="#" aria-label="Social network link"></a>
  <a class="abs social" style="left:993px" href="#" aria-label="Social network link"></a>
  <a class="abs social" style="left:1044px" href="#" aria-label="Social network link"></a>
</footer>

</body>
</html>
```